Velmora Suites Collection

I'm looking for a four page graphic design (home page, search summary/results page, apartment details page, generic information page for content such as FAQ and thank you for submitting forms etc). The pages will be used to develop a web application to promote serviced apartments throughout Africa. Although the business is based in Africa, apartments will be offered to clients across the globe. Apartments will also be situated worldwide.

Target Market(s)

Target audience is business and individual travellers looking for short stays in apartments worldwide.

Number of Pages Required

4 pages

Requirements
Must have
• Clean professional design

```html
<!DOCTYPE html>
<html lang="en">
<head>
<meta charset="utf-8">
<title>Velmora Suites Collection</title>
<link rel="stylesheet" href="https://fonts.googleapis.com/css2?family=Roboto+Condensed:wght@400;700&family=Arimo:wght@400;700&display=swap">
<style>
  :root{
    --outer:#f4f2df;
    --page:#ece5bd;
    --sidebar:#e3dcb1;
    --panel:#f4efd6;
    --navy:#1b3a6d;
    --label:#6e6646;
    --nav-top:#4c82d1;
    --nav-bottom:#2e62b2;
    --nav-line:#7da3dc;
    --btn-top:#6a6a6a;
    --btn-bottom:#474747;
    --row-a:#ddd6ac;
    --row-b:#e7e0ba;
    --footer:#a29e6f;
    --text:#2b2b2b;
  }
  *{box-sizing:border-box;margin:0;padding:0}
  html,body{width:1200px;height:1073px;overflow:hidden;background:var(--outer)}
  .stage{position:absolute;left:0;top:0;width:1024px;height:916px;transform:scale(1.171875);transform-origin:0 0;font-family:"Arimo",Arial,sans-serif;color:var(--text)}
  .page{position:absolute;left:62px;top:0;width:900px;height:916px;background:var(--page);box-shadow:0 0 6px rgba(0,0,0,.35)}
  .main-nav{position:absolute;left:62px;top:0;width:900px;height:45px;background:linear-gradient(var(--nav-top),var(--nav-bottom))}
  .main-nav ul{position:absolute;left:318px;top:0;display:flex;list-style:none;height:45px}
  .main-nav li{height:45px;display:flex;align-items:center;justify-content:center;color:#fff;font-size:16px;border-left:1px solid var(--nav-line)}
  .main-nav li:first-child{border-left:none}
  .sidebar{position:absolute;left:81px;top:0;width:300px;height:446px;background:var(--sidebar);border-radius:0 0 6px 6px;box-shadow:0 1px 4px rgba(0,0,0,.4)}
  .brand{position:absolute;left:0;top:30px;width:300px;text-align:center;font-family:"Roboto Condensed",Arial,sans-serif;font-weight:700;font-size:24px;color:var(--navy);letter-spacing:-.2px}
  .brand-rule{position:absolute;left:0;top:92px;width:300px;border-top:1px dashed #bdb68b}
  h2{font-family:"Roboto Condensed",Arial,sans-serif;font-weight:400;font-size:24px;color:var(--navy);position:absolute;letter-spacing:-.3px}
  h2 b{font-weight:700}
  .search-title{left:18px;top:104px}
  .field-label{position:absolute;left:20px;font-size:13px;font-weight:700;color:var(--label)}
  .select,.input{position:absolute;height:25px;background:#fff;border:1px solid #b8b8b8;font-size:14px;color:#777;padding:4px 7px}
  .select::after{content:"";position:absolute;right:0;top:0;width:24px;height:23px;background:#a8a8a8}
  .select svg{position:absolute;right:6px;top:8px;z-index:1}
  .btn{position:absolute;height:26px;border-radius:5px;background:linear-gradient(var(--btn-top),var(--btn-bottom));color:#fff;font-size:14px;display:flex;align-items:center;justify-content:center;box-shadow:0 1px 2px rgba(0,0,0,.3)}
  .featured{position:absolute;left:398px;top:67px;width:549px;height:379px;background:var(--panel);border-radius:7px}
  .photo{position:absolute;border:1px solid #a9a38a}
  .spec{position:absolute;font-size:12px;line-height:18px;width:190px}
  .spec div{display:flex}
  .spec dt{font-weight:700;width:109px}
  .featured .spec div{height:18px}
  .offer{position:absolute;top:516px;width:201px}
  .offer .photo{left:0;top:0;width:201px;height:81px}
  .offer .spec{left:0;top:87px;width:201px}
  .offer .spec div{height:18px}
  .offer .spec div:nth-child(odd){background:var(--row-a)}
  .offer .spec div:nth-child(even){background:var(--row-b)}
  .offer .spec dt{padding-left:9px}
  .offer .btn{left:118px;top:221px;width:82px}
  .footer{position:absolute;left:62px;top:816px;width:900px;height:100px;background:var(--footer);color:#fff;font-size:12px;padding:10px 14px;line-height:14px}
  .footer nav span{margin:0 7px}
</style>
</head>
<body>
<div class="stage">
  <div class="page"></div>

  <header class="main-nav">
    <ul>
      <li style="width:84px">Home</li>
      <li style="width:84px">Selling</li>
      <li style="width:84px">Buying</li>
      <li style="width:85px">Renting</li>
      <li style="width:74px">About</li>
      <li style="width:86px">FAQs</li>
      <li style="width:85px">Contact</li>
    </ul>
  </header>

  <aside class="sidebar">
    <div class="brand">Velmora Suites Collection</div>
    <div class="brand-rule"></div>
    <h2 class="search-title">Find an <b>Apartment</b></h2>

    <span class="field-label" style="top:148px">Country :</span>
    <div class="select" style="left:99px;top:146px;width:181px">Country<svg width="12" height="8"><path d="M0 0h12L6 8z" fill="#fff"/></svg></div>

    <span class="field-label" style="top:184px">City :</span>
    <div class="input" style="left:99px;top:182px;width:181px">-Enter a City-</div>

    <span class="field-label" style="top:219px">State :</span>
    <div class="select" style="left:98px;top:216px;width:182px">State/Province<svg width="12" height="8"><path d="M0 0h12L6 8z" fill="#fff"/></svg></div>

    <span class="field-label" style="top:257px">Prices :</span>
    <div class="select" style="left:138px;top:252px;width:141px">Min. Price<svg width="12" height="8"><path d="M0 0h12L6 8z" fill="#fff"/></svg></div>
    <div class="select" style="left:138px;top:288px;width:141px">Max. Price<svg width="12" height="8"><path d="M0 0h12L6 8z" fill="#fff"/></svg></div>

    <span class="field-label" style="top:329px">Beds :</span>
    <div class="select" style="left:151px;top:324px;width:129px">Any<svg width="12" height="8"><path d="M0 0h12L6 8z" fill="#fff"/></svg></div>

    <span class="field-label" style="top:365px">Baths :</span>
    <div class="select" style="left:150px;top:360px;width:129px">Any<svg width="12" height="8"><path d="M0 0h12L6 8z" fill="#fff"/></svg></div>

    <div class="btn" style="left:196px;top:404px;width:82px">Find Now</div>
  </aside>

  <section class="featured">
    <h2 style="left:23px;top:14px">Featured <b>Apartment</b></h2>
    <div class="photo" role="img" aria-label="Bright living room with white sofas and floor-to-ceiling windows over the water" style="left:28px;top:63px;width:277px;height:201px;background:linear-gradient(160deg,#e9d7b8 0%,#7c93b8 30%,#4e6c9a 45%,#e6e0d4 62%,#c98a45 82%,#b8743a 100%)"></div>
    <dl class="spec" style="left:342px;top:69px">
      <div><dt>City :</dt><dd>Portland</dd></div>
      <div><dt>State :</dt><dd>Oregon</dd></div>
      <div><dt>Country :</dt><dd>USA</dd></div>
      <div><dt>Beds :</dt><dd>2</dd></div>
      <div><dt>Baths :</dt><dd>2</dd></div>
      <div><dt>Square Feet :</dt><dd>4000</dd></div>
      <div><dt>Price :</dt><dd>$1500/month</dd></div>
    </dl>
    <div class="btn" style="left:444px;top:230px;width:83px">More Info</div>
    <div class="photo" role="img" aria-label="Apartment building exterior" style="left:29px;top:285px;width:72px;height:72px;background:linear-gradient(#9fb8d8 0%,#c9a27a 40%,#b07b52 75%,#5f7a3e 100%)"></div>
    <div class="photo" role="img" aria-label="Apartment building exterior" style="left:113px;top:285px;width:72px;height:72px;background:linear-gradient(#9fb8d8 0%,#c9a27a 40%,#b07b52 75%,#5f7a3e 100%)"></div>
    <div class="photo" role="img" aria-label="Apartment building exterior" style="left:197px;top:285px;width:72px;height:72px;background:linear-gradient(#9fb8d8 0%,#c9a27a 40%,#b07b52 75%,#5f7a3e 100%)"></div>
    <div class="photo" role="img" aria-label="Apartment building exterior" style="left:282px;top:285px;width:72px;height:72px;background:linear-gradient(#9fb8d8 0%,#c9a27a 40%,#b07b52 75%,#5f7a3e 100%)"></div>
    <div class="photo" role="img" aria-label="Apartment building exterior" style="left:367px;top:285px;width:72px;height:72px;background:linear-gradient(#9fb8d8 0%,#c9a27a 40%,#b07b52 75%,#5f7a3e 100%)"></div>
    <div class="photo" role="img" aria-label="Apartment building exterior" style="left:453px;top:285px;width:72px;height:72px;background:linear-gradient(#9fb8d8 0%,#c9a27a 40%,#b07b52 75%,#5f7a3e 100%)"></div>
  </section>

  <h2 style="left:84px;top:471px">Recent <b>Offers</b></h2>

  <article class="offer" style="left:84px">
    <div class="photo" role="img" aria-label="Row of cream townhouses under a blue sky" style="background:linear-gradient(#8fb3de 0%,#c9d6e6 35%,#e9dfc4 60%,#a89a80 100%)"></div>
    <dl class="spec">
      <div><dt>City :</dt><dd>Portland</dd></div><div><dt>State :</dt><dd>Oregon</dd></div><div><dt>Country :</dt><dd>USA</dd></div><div><dt>Beds :</dt><dd>2</dd></div><div><dt>Baths :</dt><dd>2</dd></div><div><dt>Square Feet :</dt><dd>4000</dd></div><div><dt>Price :</dt><dd>$1500/month</dd></div>
    </dl>
    <div class="btn">More Info</div>
  </article>

  <article class="offer" style="left:304px">
    <div class="photo" role="img" aria-label="Grey townhouses with red shutters" style="background:linear-gradient(#c7d4e2 0%,#9a9a8e 40%,#8a3b32 65%,#6f7d5a 100%)"></div>
    <dl class="spec">
      <div><dt>City :</dt><dd>Portland</dd></div><div><dt>State :</dt><dd>Oregon</dd></div><div><dt>Country :</dt><dd>USA</dd></div><div><dt>Beds :</dt><dd>2</dd></div><div><dt>Baths :</dt><dd>2</dd></div><div><dt>Square Feet :</dt><dd>4000</dd></div><div><dt>Price :</dt><dd>$1500/month</dd></div>
    </dl>
    <div class="btn">More Info</div>
  </article>

  <article class="offer" style="left:523px">
    <div class="photo" role="img" aria-label="Warm living room with a fireplace and sofa" style="background:linear-gradient(100deg,#6e2e1c 0%,#a4562e 30%,#d9b98a 55%,#8e6a4e 80%,#5a3a28 100%)"></div>
    <dl class="spec">
      <div><dt>City :</dt><dd>Portland</dd></div><div><dt>State :</dt><dd>Oregon</dd></div><div><dt>Country :</dt><dd>USA</dd></div><div><dt>Beds :</dt><dd>2</dd></div><div><dt>Baths :</dt><dd>2</dd></div><div><dt>Square Feet :</dt><dd>4000</dd></div><div><dt>Price :</dt><dd>$1500/month</dd></div>
    </dl>
    <div class="btn">More Info</div>
  </article>

  <article class="offer" style="left:742px">
    <div class="photo" role="img" aria-label="Bedroom with white bedding and wooden floor" style="background:linear-gradient(100deg,#d9a46a 0%,#c48a55 30%,#efe7dc 55%,#7a4a30 80%,#3e2a22 100%)"></div>
    <dl class="spec">
      <div><dt>City :</dt><dd>Portland</dd></div><div><dt>State :</dt><dd>Oregon</dd></div><div><dt>Country :</dt><dd>USA</dd></div><div><dt>Beds :</dt><dd>2</dd></div><div><dt>Baths :</dt><dd>2</dd></div><div><dt>Square Feet :</dt><dd>4000</dd></div><div><dt>Price :</dt><dd>$1500/month</dd></div>
    </dl>
    <div class="btn">More Info</div>
  </article>

  <footer class="footer">
    <p>Copyright © 2009 Velmora Suites Collection.</p>
    <nav>Home<span>|</span>About<span>|</span>FAQs<span>|</span>Contact</nav>
  </footer>
</div>
</body>
</html>
```